Young Makers Competition Event For Teenagers Needs Promo Graphics

I am in need of graphics for 2019 Northmere Young Makers Festival. It is a Young Makers competition event for teenagers. I need graphics to make an 11x17 poster and a main title graphic that I can use for digital (social, 16x9 for screens, etc). Graphic should include the following 2 logos: the QW Brightpath logo (this is who we are) and the "circles" logo is the logo of Young Makers Festival so that can be incorporated but is not mandatory and does not need to be in color. Tag line for Young Makers is "Discover. Develop. Deploy." Again, this is optional. Looking for an artistic design - geometric shapes, bright colors, or something along those lines. Something that speaks to teenagers and especially creatives/Young Makers types. Additionally, Post should include:
Maple Ridge Chapel
March 29-30
(registration & cost info may be added to the poster before design is finalized; still working on those details)

```html
<!DOCTYPE html>
<html lang="en">
<head>
<meta charset="utf-8">
<title>Northmere Young Makers Festival</title>
<link rel="stylesheet" href="https://fonts.googleapis.com/css2?family=Barlow+Semi+Condensed:wght@500;600&family=Kaushan+Script&family=Lato:wght@300&display=swap">
<style>
  :root {
    --paper: #ffffff;
    --sun: #f9d366;
    --blush: #ecb0ac;
    --lilac: #a5a3cc;
    --ink: #161616;
    --sky: #2aa6e4;
    --stone: #b9b6b2;
  }
  * { margin: 0; padding: 0; box-sizing: border-box; }
  html, body { width: 848px; height: 1200px; overflow: hidden; background: var(--paper); }
  .poster {
    position: relative;
    width: 848px;
    height: 1200px;
    overflow: hidden;
    background: var(--paper);
  }
  .brush-backdrop {
    position: absolute;
    inset: 0;
    background:
      linear-gradient(160deg,
        var(--ink) 0%, var(--ink) 14%,
        var(--lilac) 20%, var(--sun) 34%,
        var(--sun) 55%, var(--blush) 72%,
        var(--blush) 86%, var(--ink) 100%);
  }
  .stage-disc {
    position: absolute;
    inset: 0;
  }
  .stage-disc svg { display: block; }
  .content {
    position: absolute;
    left: 0;
    width: 848px;
    text-align: center;
  }
  .host-mark {
    top: 238px;
    display: flex;
    justify-content: center;
    align-items: center;
    gap: 10px;
    left: -6px;
    font-family: "Barlow Semi Condensed", sans-serif;
    font-weight: 600;
    font-size: 30px;
    color: var(--sky);
    letter-spacing: 0.5px;
  }
  .festival-mark {
    top: 378px;
    display: flex;
    justify-content: center;
    align-items: center;
    gap: 12px;
    left: -6px;
    font-family: "Barlow Semi Condensed", sans-serif;
    font-weight: 500;
    font-size: 22px;
    color: var(--stone);
  }
  .festival-mark .ring {
    width: 62px;
    height: 62px;
    border: 5px solid var(--stone);
    border-radius: 50%;
  }
  .host-mark .dot {
    width: 18px;
    height: 18px;
    background: var(--sky);
    border-radius: 50%;
  }
  .region {
    top: 532px;
    font-family: "Barlow Semi Condensed", sans-serif;
    font-weight: 500;
    font-size: 31px;
    color: var(--sun);
  }
  .title {
    top: 570px;
    font-family: "Kaushan Script", cursive;
    font-size: 72px;
    line-height: 1.1;
    color: var(--ink);
  }
  .tagline {
    top: 693px;
    font-family: "Barlow Semi Condensed", sans-serif;
    font-weight: 500;
    font-size: 33px;
    color: var(--sun);
  }
  .dates {
    top: 820px;
    font-family: "Barlow Semi Condensed", sans-serif;
    font-weight: 600;
    font-size: 60px;
    color: var(--blush);
    letter-spacing: 1px;
  }
  .venue {
    top: 892px;
    font-family: "Lato", sans-serif;
    font-weight: 300;
    font-size: 32px;
    color: var(--ink);
  }
</style>
</head>
<body>
<main class="poster">
  <div class="brush-backdrop" role="img" aria-label="Abstract brush strokes in black, yellow, lilac and pink scattered with black dots"></div>

  <div class="stage-disc" aria-hidden="true">
    <svg width="848" height="1200" viewBox="0 0 848 1200">
      <ellipse cx="424" cy="600" rx="384" ry="440" transform="rotate(-10 424 600)" fill="var(--paper)"/>
    </svg>
  </div>

  <div class="content host-mark"><span class="dot"></span>QW Brightpath</div>
  <div class="content festival-mark"><span class="ring"></span>Young Makers Festival</div>

  <p class="content region">Northmere</p>
  <h1 class="content title">Young Makers festival</h1>
  <p class="content tagline">Discover. Develop. Deploy</p>

  <p class="content dates">29 - 30 MARCH</p>
  <p class="content venue">Maple Ridge Chapel</p>
</main>
</body>
</html>
```